Industrial Automation company requires a business card design

Valtrin Automation provides design & build of Automated Equipment for manufacturing industry.
www.valtrinautomation.example
The equipment we design is used for manufacturing in sectors such as medical device, pharmaceutical, aerospace and electronics.
We require a new business card design which incorporates our (New) logo and the key message words:
Automated Equipment:
Design, Build, Control, Test, Support

```html
<!DOCTYPE html>
<html lang="en">
<head>
<meta charset="utf-8">
<title>Valtrin Automation – Business Card</title>
<link href="https://fonts.googleapis.com/css2?family=Open+Sans:wght@700&family=Source+Sans+3:ital,wght@0,400;0,600;1,400&display=swap" rel="stylesheet">
<style>
  :root {
    --bg: #e9e9e9;
    --card: #ffffff;
    --green: #008232;
    --ink: #111111;
    --grey: #8a8a8a;
    --shadow: rgba(0,0,0,0.18);
  }
  * { margin: 0; padding: 0; box-sizing: border-box; }
  html, body { width: 1200px; height: 1200px; overflow: hidden; background: var(--bg); }
  body { position: relative; font-family: "Source Sans 3", "Myriad Pro", sans-serif; }

  .card {
    position: absolute;
    left: 179px;
    width: 841px;
    height: 481px;
    background: var(--card);
    box-shadow: 8px 10px 14px var(--shadow);
  }
  .card--front { top: 91px; }
  .card--back { top: 617px; }

  .brand {
    position: absolute;
    display: flex;
    align-items: center;
    color: var(--green);
    font-family: "Source Sans 3", sans-serif;
    font-weight: 600;
  }
  .brand__mark { background: var(--green); flex: none; }
  .brand__name { display: flex; flex-direction: column; line-height: 1; text-transform: uppercase; }
  .brand__word { display: block; }

  .card--front .brand { left: 213px; top: 189px; gap: 20px; }
  .card--front .brand__mark { width: 70px; height: 70px; }
  .card--front .brand__word--main { font-size: 62px; letter-spacing: 4px; }
  .card--front .brand__word--sub { font-size: 20px; letter-spacing: 13px; margin-top: 6px; }

  .tagline {
    position: absolute;
    left: 99px;
    top: 375px;
    transform: translateY(-50%);
    font-family: "Open Sans", sans-serif;
    font-weight: 700;
    font-size: 18px;
    letter-spacing: 4.6px;
    color: var(--ink);
  }
  .services {
    position: absolute;
    left: 421px;
    top: 345px;
    width: 420px;
    height: 59px;
    background: var(--green);
    color: #fff;
    font-style: italic;
    font-size: 18.5px;
    display: flex;
    align-items: center;
    padding-left: 20px;
  }

  .card--back .top-band {
    position: absolute; left: 0; top: 0; width: 419px; height: 30px; background: var(--green);
  }
  .card--back .brand { left: 61px; top: 82px; gap: 12px; }
  .card--back .brand__mark { width: 46px; height: 46px; }
  .card--back .brand__word--main { font-size: 40px; letter-spacing: 3px; }
  .card--back .brand__word--sub { font-size: 13px; letter-spacing: 8.4px; margin-top: 4px; }

  .about {
    position: absolute; left: 0; width: 100%; text-align: center;
    color: var(--grey);
  }
  .about--intro { top: 197px; font-style: italic; font-size: 18px; line-height: 25px; }
  .about--sectors { top: 272px; font-weight: 600; font-size: 18.5px; line-height: 25px; }
  .sectors { color: var(--green); font-weight: 600; }

  .web-icon {
    position: absolute; left: 43px; top: 390px; width: 42px; height: 42px;
    background: var(--green); display: flex; align-items: center; justify-content: center;
  }
  .web-url {
    position: absolute; left: 102px; top: 426px; transform: translateY(-50%);
    color: var(--grey); font-weight: 600; font-size: 18.5px;
  }
</style>
</head>
<body>
  <section class="card card--front">
    <div class="brand">
      <span class="brand__mark"></span>
      <span class="brand__name">
        <span class="brand__word brand__word--main">Valtrin</span>
        <span class="brand__word brand__word--sub">Automation</span>
      </span>
    </div>
    <p class="tagline">AUTOMATED EQUIPMENT</p>
    <p class="services">DESIGN, BUILD, CONTROL, TEST, SUPPORT</p>
  </section>

  <section class="card card--back">
    <div class="top-band"></div>
    <div class="brand">
      <span class="brand__mark"></span>
      <span class="brand__name">
        <span class="brand__word brand__word--main">Valtrin</span>
        <span class="brand__word brand__word--sub">Automation</span>
      </span>
    </div>
    <p class="about about--intro">Valtrin Automation provides design &amp; build<br>of Automated Equipment for manufacturing industry.</p>
    <p class="about about--sectors">The equipment we design is used for manufacturing in sectors such as<br>
      <span class="sectors">MEDICAL DEVICE • PHARMACEUTICAL • AEROSPACE • ELECTRONICS</span></p>
    <div class="web-icon">
      <svg width="22" height="22" viewBox="0 0 22 22" fill="none" stroke="#fff" stroke-width="1.6" aria-hidden="true">
        <circle cx="11" cy="11" r="9.5"/>
        <ellipse cx="11" cy="11" rx="4.2" ry="9.5"/>
        <line x1="1.5" y1="11" x2="20.5" y2="11"/>
        <line x1="3" y1="6" x2="19" y2="6"/>
        <line x1="3" y1="16" x2="19" y2="16"/>
      </svg>
    </div>
    <p class="web-url">www.valtrinautomation.example</p>
  </section>
</body>
</html>
```